Business Card for IT company

I need a high tech looking business card using our logo. I prefer something clean and modern.

Target Market(s)

Buyers of IT hardware and software, IT Techies who are key influencers

Industry/Entity Type

Business

```html
<!DOCTYPE html>
<html lang="en">
<head>
<meta charset="utf-8">
<title>Brightfield Consulting – Business Card</title>
<link rel="stylesheet" href="https://fonts.googleapis.com/css2?family=Arimo:wght@400;700&display=swap">
<style>
  :root {
    --stage: #1e1e1e;
    --card-white: #f4f4f4;
    --charcoal: #2a2a2a;
    --charcoal-light: #4a4a4a;
    --green: #3dae2b;
    --ink: #2b2b2b;
    --muted: #555555;
  }
  * { margin: 0; padding: 0; box-sizing: border-box; }
  html, body { width: 1200px; height: 900px; overflow: hidden; }
  body {
    background: var(--stage);
    font-family: "Arimo", Arial, sans-serif;
    position: relative;
  }
  .card {
    position: absolute;
    left: 320px;
    width: 560px;
    height: 320px;
    box-shadow: 0 18px 40px rgba(0,0,0,.55);
    overflow: hidden;
  }
  /* Front */
  .card-front { top: 95px; background: var(--card-white); }
  .front-strip {
    position: absolute; left: 0; top: 0; bottom: 0; width: 118px;
    background: linear-gradient(160deg, var(--charcoal-light), var(--charcoal) 55%, #111);
  }
  .front-rule {
    position: absolute; left: 118px; top: 0; bottom: 0; width: 7px;
    background: var(--green);
  }
  .holder {
    position: absolute; right: 36px; top: 40px; text-align: right;
  }
  .holder-name { color: var(--green); font-weight: 700; font-size: 17px; }
  .holder-title { color: var(--muted); font-size: 10px; margin-top: 3px; }
  .front-wordmark {
    position: absolute; left: 160px; top: 132px;
    color: var(--ink); font-weight: 700; font-size: 26px; letter-spacing: .5px;
  }
  .contact {
    position: absolute; left: 160px; top: 196px;
    color: var(--ink); font-size: 11.5px; line-height: 1.35;
  }
  .contact p + p { margin-top: 10px; }

  /* Back */
  .card-back {
    top: 485px;
  }
  .back-pattern {
    position: absolute; inset: 0;
    background: radial-gradient(ellipse at 70% 60%, #5a5a5a, #2e2e2e 55%, #151515);
  }
  .back-wordmark {
    position: absolute; right: 42px; top: 210px;
    color: #ffffff; font-weight: 700; font-size: 26px; letter-spacing: .5px;
  }
</style>
</head>
<body>
  <section class="card card-front" aria-label="Business card front">
    <div class="front-strip" role="img" aria-label="Dark panel with repeated company name pattern"></div>
    <div class="front-rule"></div>
    <div class="holder">
      <p class="holder-name">Dorian Kessler</p>
      <p class="holder-title">General Manager</p>
    </div>
    <p class="front-wordmark">Brightfield Consulting</p>
    <div class="contact">
      <p>Brightfield Consulting, LLC<br>420 Larkspur Avenue<br>Suite 900<br>Ashford, VA 20150</p>
      <p>Main Reception: 555.210.4418<br>Office Manager: 555.210.4420/4421</p>
    </div>
  </section>

  <section class="card card-back" aria-label="Business card back">
    <div class="back-pattern" role="img" aria-label="Dark background with repeated company name pattern"></div>
    <p class="back-wordmark">Brightfield Consulting</p>
  </section>
</body>
</html>
```